Simple, elegant, business card design required

Hi designers,I am looking for a simple yet elegant business card design.

Please make use of my logo (attached); you are free to tweak the logo should you wish to do so.

Our business is involved in many different fields - almost all of them involved in some form of "design", so that's really one of the key things I want to portray. I do not wish to specify which field of design, exactly.

I prefer white on black (or just monochromatic), but if you have a different, creative idea, I am open to that too.

You can use artsy photographs provided that you have the license to use those. Please feel free to ask me any questions.
Updates

Project Deadline Extended Reason: Small extension for potential revisions. Did not get the time to provide as much feedback as I can. Added Wednesday, July 09, 2014

Target Market(s)

High-end customers looking for design consultancy

Industry/Entity Type

Business

Contact Information for Business Card

Name: Gareth Moonfield
Position: Creative Director
Mobile: +155603928174
Address: Barrow Lane, Kelmsbury upon Wren, Hallowshire GL12 4RT
Website: torvakest.com (not launched yet)

Requirements
Must have
• Design layout must be clean, original, and text must be readable when printed.
Should not have
• ~ No business card templates please. Anyone using this will be reported.
• ~ Please don't spam entries.

```html
<!DOCTYPE html>
<html lang="en">
<head>
<meta charset="utf-8">
<title>Torvakest – Business Card</title>
<link rel="stylesheet" href="https://fonts.googleapis.com/css2?family=Lato:wght@300;400;700;900&display=swap">
<style>
  :root {
    --stage: #ece8e3;
    --paper: #ffffff;
    --ink: #111111;
    --mark-grey: #8a827b;
    --on-ink: #ffffff;
    --ghost: rgba(255,255,255,0.06);
  }
  * { box-sizing: border-box; margin: 0; padding: 0; }
  html, body {
    width: 1200px; height: 1000px; overflow: hidden;
    background: var(--stage);
    font-family: "Lato", sans-serif;
  }
  .canvas { position: relative; width: 1200px; height: 1000px; }

  .card {
    position: absolute;
    width: 680px; height: 400px;
    background: var(--paper);
    box-shadow: 0 4px 14px rgba(0,0,0,0.12);
    overflow: hidden;
  }
  .card--front { left: 80px; top: 90px; }
  .card--back { left: 440px; top: 520px; }

  .brand-column {
    position: absolute; left: 0; top: 0; width: 260px; height: 100%;
    display: flex; align-items: center; justify-content: center;
  }
  .info-panel {
    position: absolute; left: 260px; top: 0; right: 0; bottom: 0;
    background: var(--ink);
    color: var(--on-ink);
    padding: 56px 30px 0 0;
    text-align: right;
  }
  .panel-notch {
    position: absolute; left: 260px; top: 186px;
    width: 0; height: 0;
    border-top: 13px solid transparent;
    border-bottom: 13px solid transparent;
    border-left: 26px solid var(--paper);
  }

  .wordmark {
    display: flex; align-items: center; gap: 10px;
    color: var(--mark-grey);
    font-weight: 900; letter-spacing: 2px;
  }
  .wordmark__dot {
    width: 18px; height: 18px; border-radius: 50%;
    background: var(--mark-grey);
  }
  .wordmark--card { font-size: 28px; }
  .wordmark--back { font-size: 34px; }

  .person-name { font-size: 28px; font-weight: 300; line-height: 1; }
  .person-name strong { font-weight: 700; }
  .person-role { font-size: 14px; font-weight: 700; margin-top: 3px; }

  .address {
    margin-top: 28px; font-size: 18px; line-height: 1.3; font-weight: 400;
  }
  .address strong { font-weight: 700; }
  .address svg { vertical-align: -2px; margin-right: 6px; }

  .phone {
    margin-top: 30px; font-size: 27px; font-weight: 700; letter-spacing: 0.3px;
  }
  .phone svg { vertical-align: -3px; margin-right: 4px; }

  .website { margin-top: 32px; font-size: 18px; font-weight: 400; }

  .ghost-name {
    position: absolute; right: 30px; bottom: 26px;
    font-size: 30px; font-weight: 900; letter-spacing: 4px;
    color: var(--ghost);
  }

  .card--back .wordmark {
    position: absolute; right: 60px; top: 50%; transform: translateY(-50%);
  }

  .presentation-mark {
    position: absolute; left: 40px; top: 880px;
    color: var(--ink); font-size: 34px; font-weight: 400; letter-spacing: 5px;
    display: flex; align-items: center; gap: 12px;
  }
  .presentation-mark .wordmark__dot { background: var(--ink); width: 20px; height: 20px; }
</style>
</head>
<body>
<main class="canvas">

  <section class="card card--front" aria-label="Business card front">
    <div class="brand-column">
      <div class="wordmark wordmark--card"><span class="wordmark__dot"></span>TORVAKEST</div>
    </div>
    <div class="info-panel">
      <p class="person-name">Gareth <strong>Moonfield</strong></p>
      <p class="person-role">Creative Director</p>
      <p class="address">
        <svg width="11" height="15" viewBox="0 0 11 15" aria-hidden="true"><path d="M5.5 0C2.5 0 0 2.4 0 5.4 0 9.5 5.5 15 5.5 15S11 9.5 11 5.4C11 2.4 8.5 0 5.5 0zm0 7.6a2.2 2.2 0 1 1 0-4.4 2.2 2.2 0 0 1 0 4.4z" fill="#fff"/></svg>Barrow Lane, Kelmsbury upon Wren<br>
        Hallowshire <strong>GL12 4RT.</strong>
      </p>
      <p class="phone">
        <svg width="14" height="22" viewBox="0 0 14 22" aria-hidden="true"><rect x="1" y="4" width="12" height="17" rx="2" fill="#fff"/><rect x="3" y="7" width="8" height="5" fill="#111"/><rect x="9" y="0" width="2" height="5" fill="#fff"/></svg>+155603928174
      </p>
      <p class="website">www.torvakest.com</p>
      <span class="ghost-name" aria-hidden="true">TORVAKEST</span>
    </div>
    <span class="panel-notch" aria-hidden="true"></span>
  </section>

  <section class="card card--back" aria-label="Business card back">
    <div class="wordmark wordmark--back"><span class="wordmark__dot"></span>TORVAKEST</div>
  </section>

  <div class="presentation-mark"><span class="wordmark__dot"></span>TORVAKEST</div>

</main>
</body>
</html>
```